Bref créative
Corvane Oral Care Stationary
Corvane Oral Care
Professional
R. Lucien Dorvash, DDS, MAGD
2483 W Perrin Ave.
Baytown, TX 77520
dentist@qbl.zx.com
www.corvaneoralcare.com

```html
<!DOCTYPE html>
<html lang="en">
<head>
<meta charset="utf-8">
<title>Corvane Oral Care – Business Card</title>
<link rel="stylesheet" href="https://fonts.googleapis.com/css2?family=Tinos:wght@400;700&display=swap">
<style>
  :root {
    --paper: #ffffff;
    --band-green: #5f9b3c;
    --band-olive: #4f7f5a;
    --band-navy: #2d3a8c;
    --swoosh-grey: #a6a8ab;
    --ink: #1f1f1f;
    --header-ink: #ffffff;
    --brand-teal: #2e6f88;
  }
  html, body {
    margin: 0;
    padding: 0;
    overflow: hidden;
    background: var(--paper);
  }
  .card {
    position: relative;
    width: 1200px;
    height: 686px;
    background: var(--paper);
    overflow: hidden;
    font-family: "Tinos", "Times New Roman", serif;
    color: var(--ink);
  }
  .card__header-art {
    position: absolute;
    inset: 0;
    width: 1200px;
    height: 686px;
  }
  .holder {
    position: absolute;
    top: 26px;
    right: 42px;
    text-align: right;
    color: var(--header-ink);
  }
  .holder__name {
    margin: 0;
    font-size: 30px;
    font-weight: 700;
    line-height: 1.2;
  }
  .holder__title {
    margin: 4px 0 0;
    font-size: 29px;
    font-weight: 400;
    line-height: 1.2;
  }
  .brand {
    position: absolute;
    left: 48px;
    top: 300px;
    display: flex;
    align-items: center;
    gap: 18px;
  }
  .brand__dot {
    width: 46px;
    height: 46px;
    border-radius: 50%;
    background: var(--brand-teal);
  }
  .brand__name {
    margin: 0;
    font-size: 44px;
    font-weight: 700;
    line-height: 1.05;
    color: var(--brand-teal);
  }
  .address {
    position: absolute;
    left: 43px;
    top: 572px;
    margin: 0;
    font-style: normal;
    font-size: 25px;
    line-height: 41px;
  }
  .contact {
    position: absolute;
    right: 42px;
    text-align: right;
    margin: 0;
    font-size: 25px;
    line-height: 34px;
  }
  .contact--lines { top: 478px; }
  .contact--online { top: 580px; }
</style>
</head>
<body>
  <div class="card">
    <svg class="card__header-art" viewBox="0 0 1200 686" aria-hidden="true">
      <defs>
        <linearGradient id="bandGradient" x1="0" y1="0" x2="1" y2="0">
          <stop offset="0" stop-color="var(--band-green)"/>
          <stop offset="0.45" stop-color="var(--band-olive)"/>
          <stop offset="1" stop-color="var(--band-navy)"/>
        </linearGradient>
      </defs>
      <path class="swoosh-grey" fill="var(--swoosh-grey)"
            d="M430,50 C700,92 950,168 1200,170 V206 C950,198 700,118 430,50 Z"/>
      <path class="header-band" fill="url(#bandGradient)"
            d="M0,0 H1200 V166 C930,152 640,62 400,42 C220,27 90,22 0,28 Z"/>
    </svg>

    <header class="holder">
      <p class="holder__name">R. Lucien Dorvash</p>
      <p class="holder__title">DDS, MAGD</p>
    </header>

    <div class="brand">
      <span class="brand__dot"></span>
      <p class="brand__name">Corvane<br>Oral Care</p>
    </div>

    <address class="address">
      2483 W Perrin Ave.<br>
      Baytown, TX 77520
    </address>

    <p class="contact contact--lines">
      Phone : 281-555-0142<br>
      Fax : 281-555-0187
    </p>

    <p class="contact contact--online">
      Email : dentist@qbl.zx.com<br>
      Web : www.corvaneoralcare.com
    </p>
  </div>
</body>
</html>
```